Tovell Family Law, legal technician needs a website and design

I need a website for a family law practice. I specialize in collaborative law, unbundled services, and mediation. The website must contain my company logo (file attached), and the website must be a mixture of my personality and my profession. I have attached additional information to explain my personality and profession.

Target Market(s)

Lower through middle-class (income level up to $200,000 per year)

Coding

Coded - Design and coding required

Number of Pages Required

1 page

Requirements
Must have
• Must have enough pages to cover required content. I submitted below some content about the collaborative law process. All of the content is not necessary. However, the website must have enough content to clearly describe the services I offer. Use your professionalism and judgment regarding font, font size, etc.

```html
<!DOCTYPE html>
<html lang="en">
<head>
<meta charset="utf-8">
<title>Tovell Family Law</title>
<link rel="stylesheet" href="https://fonts.googleapis.com/css2?family=Cinzel:wght@400;600&family=Crimson+Text:wght@400;600&family=Poppins:wght@400&display=swap">
<style>
:root{
  --gold:#c4bd45;
  --gold-dark:#7d7818;
  --ink:#111111;
  --night:#1d1e25;
  --slate:#2b2e3b;
  --slate-deep:#1f2028;
  --mist:#f2f2f2;
  --canvas:#f4f4f4;
  --text-light:#e6e6e6;
  --text-body:#333333;
}
*{box-sizing:border-box;margin:0;padding:0}
html,body{width:1200px;height:3409px;overflow:hidden;background:var(--canvas)}
body{font-family:"Crimson Text",Georgia,serif;color:var(--text-body)}
.page{position:absolute;left:109px;top:73px;width:982px;height:3264px;background:#fff;overflow:hidden}
.abs{position:absolute}
.heading{font-family:"Cinzel",Georgia,serif}

/* header / hero */
.hero{left:0;top:0;width:982px;height:526px;background:linear-gradient(180deg,#262b3c 0%,#1f2333 45%,#2a2c33 80%,#3a3a30 100%)}
.brand{left:52px;top:26px;display:flex;align-items:center;gap:8px;color:var(--gold);font-family:"Crimson Text",serif;font-size:15px;letter-spacing:1px;text-transform:uppercase}
.brand .mark{width:14px;height:14px;border:1.5px solid var(--gold)}
.nav{top:35px;font-size:11.5px;color:var(--gold);letter-spacing:.5px;text-transform:uppercase}
.nav-rule{left:0;top:75px;width:982px;height:1px;background:rgba(196,189,69,.35)}
.hero-title{left:0;width:982px;top:234px;text-align:center;color:#fff;font-size:46px;font-weight:400;letter-spacing:1px}
.hero-sub{left:0;width:982px;top:297px;text-align:center;color:var(--gold);font-size:14.5px;line-height:18px}
.btn{display:block;background:linear-gradient(180deg,#b5ae33,#6f6b14);color:#fff;text-align:center;font-size:14px}
.hero-btn{left:416px;top:355px;width:154px;height:34px;line-height:34px;background:#aaa42d;font-weight:600}

.feature{top:462px;width:192px;height:261px;text-align:center;color:var(--text-light)}
.feature:nth-child(odd){background:var(--slate)}
.feature:nth-child(even){background:var(--slate-deep)}
.feature .badge{position:absolute;left:86px;top:24px;width:20px;height:20px;border:1.5px solid var(--gold)}
.feature h3{position:absolute;left:0;width:100%;top:65px;font-family:"Crimson Text",serif;font-weight:400;font-size:17px;color:var(--gold);letter-spacing:.5px}
.feature .rule{position:absolute;left:76px;top:98px;width:40px;height:1px;background:var(--gold)}
.feature p{position:absolute;left:20px;width:152px;top:114px;font-size:12px;line-height:14.4px}
.feature .outline{position:absolute;left:62px;top:220px;width:68px;height:19px;border:1px solid var(--gold);color:var(--gold);font-size:10px;line-height:17px}

/* about */
.ghost{color:rgba(0,0,0,.14);font-family:"Cinzel",serif;font-weight:600;white-space:nowrap}
.ghost-light{color:rgba(255,255,255,.06)}
.about-ghost{left:86px;top:816px;font-size:58px}
.about-title{left:117px;top:832px;font-size:37px;font-weight:400;color:var(--ink)}
.kicker{font-family:"Crimson Text",serif;font-size:18px;color:var(--ink);text-transform:uppercase;letter-spacing:.3px}
.kicker span{color:var(--gold)}
.about-kicker{left:117px;top:888px}
.about-copy{left:117px;top:912px;width:362px;font-size:14.5px;line-height:17.8px;color:#3a3a3a}
.about-mark{left:575px;top:804px;width:311px;height:322px;display:flex;align-items:center;justify-content:center;text-align:center;color:var(--gold);font-family:"Crimson Text",serif;font-size:44px;line-height:50px;font-weight:600}

/* services */
.services{left:0;top:1204px;width:982px;height:245px;background:var(--night)}
.services-ghost{left:0;width:982px;text-align:center;top:1225px;font-size:58px}
.services-title{left:0;width:982px;text-align:center;top:1245px;font-size:36px;color:var(--gold);font-weight:600}
.service{top:1339px;width:220px;height:285px;background:var(--slate);color:var(--text-light);text-align:center;box-shadow:0 4px 10px rgba(0,0,0,.25)}
.service:nth-of-type(2){background:var(--slate-deep)}
.service svg{position:absolute;left:87px;top:16px}
.service h3{position:absolute;left:0;width:100%;top:76px;font-family:"Crimson Text",serif;font-size:15px;font-weight:600;color:#fff}
.service p{position:absolute;left:30px;width:160px;top:114px;font-size:11.8px;line-height:14.4px}
.service .more{position:absolute;right:24px;top:258px;color:var(--gold);font-size:12px;font-weight:600}

/* practice */
.practice-photo{left:109px;top:1728px;width:311px;height:305px;background:linear-gradient(135deg,#2a2a2a,#141414 55%,#4a3b2a);border-radius:3px}
.practice-photo::after{content:"";position:absolute;left:16px;top:14px;right:16px;bottom:14px;border:1px solid var(--gold);border-radius:3px}
.practice-ghost{left:476px;top:1733px;font-size:60px}
.practice-title{left:496px;top:1752px;font-size:34px;font-weight:400;color:var(--ink)}
.practice-kicker{left:498px;top:1797px}
.practice-copy{left:498px;top:1830px;width:440px;font-size:14.5px;line-height:17.8px;color:#333}
.practice-btn{left:498px;top:1988px;width:113px;height:32px;line-height:32px;font-size:13px}

/* mediation */
.mediation{left:0;top:2122px;width:982px;height:339px;background:var(--night)}
.mediation-ghost{left:56px;top:2186px;font-size:44px}
.mediation-title{left:87px;top:2186px;font-size:32px;color:var(--gold);font-weight:600}
.mediation-copy{left:88px;width:540px;color:var(--text-light);font-size:14.5px;line-height:18px}
.mediation-btn{left:89px;top:2391px;width:111px;height:32px;line-height:32px;font-size:13px}
.portrait{left:679px;top:2026px;width:258px;height:435px;background:linear-gradient(180deg,#5a4a3e 0%,#b9c9dd 30%,#95aac4 70%,#2c3444 100%);border-radius:120px 120px 0 0}

/* testimonials */
.testimonials{left:0;top:2461px;width:982px;height:481px;background:var(--mist)}
.testi-ghost{left:0;width:982px;text-align:center;top:2522px;font-size:52px;color:rgba(0,0,0,.13)}
.testi-title{left:0;width:982px;text-align:center;top:2534px;font-size:32px;font-weight:600;color:var(--ink)}
.quote{top:2616px;width:336px;height:172px;background:#fff;box-shadow:0 2px 8px rgba(0,0,0,.12)}
.quote::after{content:"";position:absolute;left:48px;bottom:-18px;border-left:0 solid transparent;border-right:26px solid transparent;border-top:18px solid #fff}
.quote .qmark{position:absolute;left:36px;top:18px;font-family:Georgia,serif;font-size:54px;line-height:54px;color:var(--gold);font-weight:700}
.quote p{position:absolute;left:30px;top:56px;width:284px;font-size:11.8px;line-height:17px;color:#444;text-indent:54px}
.avatar{top:2824px;width:52px;height:52px;border-radius:50%;background:linear-gradient(180deg,#d9cbbd,#8f7766)}
.reviewer{top:2829px;font-size:12px;line-height:13px;color:#333}
.reviewer .stars{color:#e0b72a;font-size:10px;letter-spacing:1px}
.arrow{top:2690px}

/* footer */
.footer{left:0;top:2942px;width:982px;height:322px;background:#111}
.foot-brand{left:84px;top:3000px;width:80px;height:80px;border:1.5px solid #fff;border-radius:50%;display:flex;align-items:center;justify-content:center;text-align:center;color:#fff;font-size:12px;line-height:14px}
.foot-note{left:52px;top:3090px;width:170px;color:#ddd;font-size:10px;line-height:12px}
.foot-head{top:2998px;color:#fff;font-size:21px;font-weight:400;font-family:"Crimson Text",serif;letter-spacing:.5px;text-transform:uppercase}
.foot-links{left:248px;top:3038px;list-style:none;color:#fff;font-size:13px;line-height:26px;text-transform:uppercase}
.contact-item{left:438px;color:#fff;font-size:13px;line-height:16px;display:flex;gap:14px}
.contact-item svg{flex:none;margin-top:1px}
.field{background:#fff;border:1px solid #ccc;font-family:"Poppins",sans-serif;font-size:8.5px;color:#999;padding:5px 6px}
.submit{left:656px;top:3162px;width:91px;height:22px;line-height:22px;background:#a9a22c;color:#fff;font-family:"Poppins",sans-serif;font-size:10px;text-align:center}
.foot-rule{left:119px;top:3231px;width:746px;height:1px;background:#555}
.copyright{left:0;width:982px;top:3240px;text-align:center;color:#ddd;font-family:"Poppins",sans-serif;font-size:9.5px}
</style>
</head>
<body>
<div class="page">

  <!-- hero -->
  <section class="abs hero" role="img" aria-label="City skyline at dusk with a tall needle tower under a cloudy sky, darkened"></section>
  <div class="abs brand"><span class="mark"></span>Tovell Family Law</div>
  <nav>
    <a class="abs nav" style="left:302px">Home</a>
    <a class="abs nav" style="left:379px">About Us</a>
    <a class="abs nav" style="left:469px">Services</a>
    <a class="abs nav" style="left:556px">Practice Areas</a>
    <a class="abs nav" style="left:686px">Process</a>
    <a class="abs nav" style="left:771px">Mediation</a>
    <a class="abs nav" style="left:869px">Contact Us</a>
  </nav>
  <div class="abs nav-rule"></div>

  <svg class="abs" style="left:452px;top:150px" width="78" height="70" viewBox="0 0 78 70" fill="none" stroke="#c4bd45" stroke-width="3">
    <line x1="39" y1="6" x2="39" y2="62"/><line x1="8" y1="16" x2="70" y2="16"/>
    <path d="M12 16 L2 40 H22 Z"/><path d="M66 16 L56 40 H76 Z"/>
    <path d="M26 62 H52" stroke-width="6"/>
  </svg>
  <h1 class="abs heading hero-title">TOVELL FAMILY LAW</h1>
  <p class="abs hero-sub">Lorem Ipsum Dolor Sit Amet&nbsp; Consectetur Adipiscing Elit Tellus Neque Feugiat Sit Justo, Nec Nisl, Sed.<br>Tristique Urna Tellus Erat Suscipit Vulputate Integer Vitae.</p>
  <a class="abs btn hero-btn">View Practice Areas</a>

  <div class="abs" style="left:123px;top:0">
    <div class="abs feature" style="left:0"><span class="badge"></span><h3>FAMILY LAW</h3><span class="rule"></span><p>Lorem Ipsum Dolor Sit Amet Consectetur Adipiscing Elit Tellus Neque Feugiat Sit Justo, Nec Nisl, Sed. Tristique Urna Tellus Erat Suscipit Vulputate Integer Vitae.</p><span class="outline">Learn More</span></div>
    <div class="abs feature" style="left:192px"><span class="badge"></span><h3>FAMILY LAW</h3><span class="rule"></span><p>Lorem Ipsum Dolor Sit Amet Consectetur Adipiscing Elit Tellus Neque Feugiat Sit Justo, Nec Nisl, Sed. Tristique Urna Tellus Erat Suscipit Vulputate Integer Vitae.</p><span class="outline">Learn More</span></div>
    <div class="abs feature" style="left:384px"><span class="badge"></span><h3>FAMILY LAW</h3><span class="rule"></span><p>Lorem Ipsum Dolor Sit Amet Consectetur Adipiscing Elit Tellus Neque Feugiat Sit Justo, Nec Nisl, Sed. Tristique Urna Tellus Erat Suscipit Vulputate Integer Vitae.</p><span class="outline">Learn More</span></div>
    <div class="abs feature" style="left:576px"><span class="badge"></span><h3>FAMILY LAW</h3><span class="rule"></span><p>Lorem Ipsum Dolor Sit Amet Consectetur Adipiscing Elit Tellus Neque Feugiat Sit Justo, Nec Nisl, Sed. Tristique Urna Tellus Erat Suscipit Vulputate Integer Vitae.</p><span class="outline">Learn More</span></div>
  </div>

  <!-- about -->
  <div class="abs ghost about-ghost">ABOUT US</div>
  <h2 class="abs heading about-title">ABOUT US</h2>
  <p class="abs kicker about-kicker">What Is <span>Collaborative Law?</span></p>
  <p class="abs about-copy">Every Year, Hundreds Of Thousands Of Marriages End In Divorce. Are You In This Situation Right Now? Are You Getting Ready To Hire A Lawyer To Help You With Your Case?<br>If So, Before You Make A Decision On The Process You Are Choosing For Your Divorce Process, Read On To Learn More About The Collaborative Approach To Divorce And You Will Discover The Benefits This Process Offers.&nbsp; When You Are Done Reading This Post You Will See Why So Many Divorcing Couples Choose The Collaborative Process For Their Divorce.</p>
  <div class="abs about-mark">Tovell<br>Family Law</div>

  <!-- services -->
  <section class="abs services" role="img" aria-label="Dark backdrop of a law library"></section>
  <div class="abs ghost ghost-light services-ghost">OUR SERVICES</div>
  <h2 class="abs heading services-title">OUR SERVICES</h2>
  <article class="abs service" style="left:142px">
    <svg width="46" height="46" viewBox="0 0 46 46" fill="none" stroke="#c4bd45" stroke-width="2"><rect x="10" y="6" width="18" height="9" transform="rotate(45 19 10)"/><line x1="22" y1="18" x2="38" y2="34"/><rect x="4" y="38" width="22" height="5"/></svg>
    <h3>Lorem Ipsum</h3>
    <p>Lorem Ipsum Dolor Sit Amet Consectetur Adipiscing Elit Tellus Neque Feugiat Sit Justo, Nec Nisl, Sed. Tristique Urna Tellus Erat Suscipit Vulputate Integer Vitae.Urna Tellus Erat Suscipit Vulputate Integer Vitae.Urna Tellus Erat Suscipit Vulputate Integer Vitae.</p>
    <span class="more">Read More</span>
  </article>
  <article class="abs service" style="left:382px">
    <svg width="46" height="46" viewBox="0 0 46 46" fill="none" stroke="#c4bd45" stroke-width="2"><path d="M4 16 L23 4 L42 16 Z"/><line x1="10" y1="18" x2="10" y2="36"/><line x1="18" y1="18" x2="18" y2="36"/><line x1="28" y1="18" x2="28" y2="36"/><line x1="36" y1="18" x2="36" y2="36"/><rect x="4" y="38" width="38" height="5"/></svg>
    <h3>Lorem Ipsum</h3>
    <p>Lorem Ipsum Dolor Sit Amet Consectetur Adipiscing Elit Tellus Neque Feugiat Sit Justo, Nec Nisl, Sed. Tristique Urna Tellus Erat Suscipit Vulputate Integer Vitae. Urna Tellus Erat Suscipit Vulputate Integer Vitae.Urna Tellus Erat Suscipit Vulputate Integer Vitae.</p>
    <span class="more">Read More</span>
  </article>
  <article class="abs service" style="left:622px">
    <svg width="46" height="46" viewBox="0 0 46 46" fill="none" stroke="#c4bd45" stroke-width="2"><line x1="23" y1="4" x2="23" y2="40"/><line x1="6" y1="12" x2="40" y2="12"/><path d="M8 12 L2 26 H14 Z"/><path d="M38 12 L32 26 H44 Z"/><line x1="14" y1="42" x2="32" y2="42"/></svg>
    <h3>Lorem Ipsum</h3>
    <p>Lorem Ipsum Dolor Sit Amet Consectetur Adipiscing Elit Tellus Neque Feugiat Sit Justo, Nec Nisl, Sed. Tristique Urna Tellus Erat Suscipit Vulputate Integer Vitae. Urna Tellus Erat Suscipit Vulputate Integer Vitae.Urna Tellus Erat Suscipit Vulputate Integer Vitae.</p>
    <span class="more">Read More</span>
  </article>

  <!-- practice -->
  <div class="abs practice-photo" role="img" aria-label="Lawyer at a desk with a gavel and documents, a gold scales of justice overlay"></div>
  <div class="abs ghost practice-ghost">PRACTICE</div>
  <h2 class="abs heading practice-title">OUR PRACTICE</h2>
  <p class="abs kicker practice-kicker">What Is <span>Collaborative Practice?</span></p>
  <p class="abs practice-copy">Collaborate Practice&nbsp; Is A Process Where Trained Professionals, Including Attorneys, Help Couples Resolve Their Disputes Without Litigation And Outside Of Court.&nbsp;&nbsp; Instead, Those Involved In The Case Approach The Legal Process Through The Lens Of Teamwork, Trouble-Shooting, And Problem-Solving Rather Than Fighting To “Beat” Someone Else.&nbsp; Another Way Of Describing This Process Is Rather Than Looking At A “Win – Lose” Result, See It As Awin-Win” For All Involved.</p>
  <a class="abs btn practice-btn">Learn More</a>

  <!-- mediation -->
  <section class="abs mediation"></section>
  <div class="abs ghost ghost-light mediation-ghost">MEDIATION</div>
  <h2 class="abs heading mediation-title">OUR MEDIATION</h2>
  <p class="abs mediation-copy" style="top:2230px">Mediation To Help You Reach An Agreement $250 Per Hour, Available</p>
  <p class="abs mediation-copy" style="top:2265px">In Addition To The Above Packages, We Offer The Following Services, Which Can Be Adapted To Your Individual Situation:</p>
  <p class="abs mediation-copy" style="top:2318px">&nbsp;If You Both Agree And You Have Already Filled Out Your Own Divorce Forms - Divorce Form Review $250 Flat Fee For A One-Time Review, Research, And Recommendations</p>
  <a class="abs btn mediation-btn">View More</a>
  <div class="abs portrait" role="img" aria-label="Smiling attorney in a light blue shirt and dark tie with arms crossed"></div>

  <!-- testimonials -->
  <section class="abs testimonials"></section>
  <div class="abs ghost testi-ghost">TESTIMONIAL</div>
  <h2 class="abs heading testi-title">OUR TESTIMONIAL</h2>
  <svg class="abs arrow" style="left:72px" width="34" height="20" viewBox="0 0 34 20" fill="none" stroke="#b5ae33" stroke-width="2"><line x1="2" y1="10" x2="32" y2="10"/><polyline points="10,3 2,10 10,17"/></svg>
  <svg class="abs arrow" style="left:878px" width="34" height="20" viewBox="0 0 34 20" fill="none" stroke="#b5ae33" stroke-width="2"><line x1="2" y1="10" x2="32" y2="10"/><polyline points="24,3 32,10 24,17"/></svg>
  <div class="abs quote" style="left:144px"><span class="qmark">“</span><p>Lorem Ipsum Dolor Sit Amet, Consectetur Adipiscing Odio Ultrices Amet, Congue Integer Any Nibh. Amet, Eget Tristique Vitae A Sed Venenatis. Dictumst Eros Id Vitae Orci Id. Senectus Senectus Parturient Any Time&nbsp; Diam, Namtristique Vitae A Sed Venenatis. Dictumst Dictumst Dictumst Eros Id</p></div>
  <div class="abs quote" style="left:503px"><span class="qmark">“</span><p>Lorem Ipsum Dolor Sit Amet, Consectetur Adipiscing Odio Ultrices Amet, Congue Integer Any Nibh. Amet, Eget Tristique Vitae A Sed Venenatis. Dictumst Eros Id Vitae Orci Id. Senectus Senectus Parturient Any Time&nbsp; Diam, Namtristique Vitae A Sed Venenatis. Dictumst Dictumst Dictumst Eros Id</p></div>
  <div class="abs avatar" style="left:141px" role="img" aria-label="Client portrait"></div>
  <div class="abs reviewer" style="left:202px">Lorem Ipsum<br>Lorem Ipsum<br><span class="stars">★★★★★</span></div>
  <div class="abs avatar" style="left:502px" role="img" aria-label="Client portrait"></div>
  <div class="abs reviewer" style="left:565px">Lorem Ipsum<br>Lorem Ipsum<br><span class="stars">★★★★★</span></div>

  <!-- footer -->
  <footer class="abs footer"></footer>
  <div class="abs foot-brand">Tovell<br>Family Law</div>
  <p class="abs foot-note">As You Can See, There Are Plenty Of Reasons To Consider Collaborative Practice.</p>
  <h4 class="abs foot-head" style="left:245px">Quick Links</h4>
  <ul class="abs foot-links"><li>Home</li><li>About Us</li><li>Practice Areas</li><li>Process</li><li>Mediation</li><li>Contact Us</li></ul>
  <h4 class="abs foot-head" style="left:438px">Contact Us</h4>
  <div class="abs contact-item" style="top:3048px"><svg width="13" height="13" viewBox="0 0 24 24" fill="#c4bd45"><path d="M6.6 10.8a15 15 0 006.6 6.6l2.2-2.2a1 1 0 011-.25 11.4 11.4 0 003.6.6 1 1 0 011 1V20a1 1 0 01-1 1A17 17 0 013 4a1 1 0 011-1h3.5a1 1 0 011 1 11.4 11.4 0 00.6 3.6 1 1 0 01-.25 1z"/></svg>5550-1234-88</div>
  <div class="abs contact-item" style="top:3074px"><svg width="13" height="13" viewBox="0 0 24 24" fill="none" stroke="#c4bd45" stroke-width="2"><rect x="2" y="5" width="20" height="14"/><polyline points="2,5 12,13 22,5"/></svg>Admin@tovellcollab.com</div>
  <div class="abs contact-item" style="top:3100px"><svg width="13" height="13" viewBox="0 0 24 24" fill="#c4bd45"><path d="M22 2 L2 10 L11 13 L14 22 Z"/></svg>Suite 12, 88 Harbor Lane,<br>Portland OR</div>
  <h4 class="abs foot-head" style="left:656px">Get In Touch</h4>
  <div class="abs field" style="left:656px;top:3031px;width:131px;height:22px">Name</div>
  <div class="abs field" style="left:800px;top:3031px;width:130px;height:22px">Phone number</div>
  <div class="abs field" style="left:656px;top:3063px;width:131px;height:22px">Subject</div>
  <div class="abs field" style="left:800px;top:3063px;width:130px;height:22px">Email</div>
  <div class="abs field" style="left:656px;top:3096px;width:274px;height:49px">Message</div>
  <div class="abs submit">SUBMIT</div>
  <div class="abs foot-rule"></div>
  <p class="abs copyright">COPYRIGHTS © 2021 TOVELL FAMILY LAW. ALL RIGHTS RESERVED. TERMS &amp; CONDITIONS</p>
</div>
</body>
</html>
```